Productos de Embalaje, todo lo que necesitas en un solo lugar.

Hola, somos una empresa ubicada en Monterrey, México, comercializamos productos empaques industriales, de entrada no se si quiera si el titulo del proyecto es el correcto, este saldrá supongo en el folleto?, no sé si necesitamos un brochure o un flyer, no se las diferencias, por eso me acerco a ustedes, soy malo para el diseño.

Favor de basarse en nuestra página web www.lumvexa.com, de ahi se pueden sacar textos, colores, etc, adjunto logo, imagenes que pueden servirles de nuestros productos, así como un ejemplo de brochure que vi, se ve padre.

Quiero hacer crecer mi negocio y buscar clientes potenciales por correo principalmente. así como presencial, por lo que se requiere enviarse por correo o imprimir, el proyecto es 100% español.

Queremos algo atractivo, fresco, profesional

____________________________________________

Hello, we are a micro company located in Monterrey, Mexico, I do not know if we need a brochure or a flyer, we specialize in marketing products for Industrial Packaging, I want to grow my business and look for potential customers by mail mainly, as well as face-to-face, by What this design is required can be sent by mail or printed, we want something eye-catching, fresh, professional.
Our web page is www.lumvexa.com , already attach a brochure example that is good.

Target Market(s)

Clientes de habla hispana, favor de checar mi página www.lumvexa.com

Industry/Entity Type

Industrial

Requirements
Must have
• Contacto:
• Teléfono: (81) 4715-2083
• Correo: ventas@lumvexa.com
• Valle Arenal, Sierra Alta, México.
• instagram y facebook
• @LUMVEXAMTY
• @lumvexamty
Nice to have
• Estoy abierto, proporcione un brochure de ejemplo que me gusto, pero acepto diseños diferentes, www.lumvexa.com
Should not have
• English.

```html
<!DOCTYPE html>
<html lang="es">
<head>
<meta charset="utf-8">
<title>LUMVEXA · Empaque Industrial</title>
<link href="https://fonts.googleapis.com/css2?family=Oswald:wght@500;700&family=PT+Sans:wght@400&display=swap" rel="stylesheet">
<style>
  :root {
    --yellow: #e0b31c;
    --gray: #a3a3a3;
    --ink: #1e1e1e;
    --paper: #ffffff;
    --backdrop: #6a6a6a;
    --icon: #4a4a4a;
    --wrap-tone: linear-gradient(160deg, #f4f4f4, #cfcfcf 60%, #e9e9e9);
    --wood-tone: linear-gradient(150deg, #c89a62, #a0703c 55%, #e0c39a);
    --foam-tone: linear-gradient(120deg, #b07a4a 0%, #9d6c3f 30%, #dcdcdc 45%, #f6f6f6 70%, #bfbfbf);
    --pallet-tone: linear-gradient(180deg, #efefef 0%, #e0e0e0 30%, #d9b07a 50%, #c4935a 75%, #ececec);
  }
  * { margin: 0; padding: 0; box-sizing: border-box; }
  html, body { width: 1200px; height: 1200px; overflow: hidden; background: var(--backdrop); }
  .flyer {
    position: absolute; left: 218px; top: 66px;
    width: 763px; height: 1070px; background: var(--paper); overflow: hidden;
    font-family: "PT Sans", sans-serif; color: var(--ink);
  }
  .photo { position: absolute; left: 0; width: 381px; }
  .photo--wrap { top: 0; height: 262px; background: var(--wrap-tone); }
  .photo--wood { top: 270px; height: 258px; background: var(--wood-tone); }
  .photo--foam { top: 538px; height: 264px; background: var(--foam-tone); }
  .photo--pallet { top: 810px; height: 260px; background: var(--pallet-tone); }

  .brand { position: absolute; left: 405px; top: 34px; }
  .brand__name {
    font-family: "Oswald", sans-serif; font-weight: 700; font-size: 70px;
    letter-spacing: -1px; line-height: 1; color: var(--gray);
  }
  .brand__tag { font-size: 17px; color: var(--gray); letter-spacing: 1px; margin-top: 2px; }

  .section { position: absolute; left: 403px; width: 326px; }
  .section__title {
    font-family: "Oswald", sans-serif; font-weight: 700; font-size: 30px;
    color: var(--yellow); line-height: 1; letter-spacing: -0.5px;
  }
  .section__bar { width: 65px; height: 3px; background: var(--gray); margin-top: 6px; }
  .section__text {
    font-size: 14.6px; line-height: 19.4px; text-align: justify; margin-top: 20px;
  }
  .values { list-style: none; display: grid; grid-template-columns: 166px 160px; row-gap: 6px; margin-top: 22px; padding-left: 16px; }
  .values li { font-size: 17px; line-height: 21px; padding-left: 16px; position: relative; }
  .values li::before {
    content: ""; position: absolute; left: 0; top: 7px; width: 6px; height: 6px;
    border-radius: 50%; background: var(--yellow);
  }

  .contact-band {
    position: absolute; left: 0; top: 944px; width: 763px; height: 91px;
    background: var(--yellow); color: #fff;
  }
  .contact-phone {
    position: absolute; left: 30px; top: 26px; display: flex; align-items: center; gap: 10px;
    font-family: "Oswald", sans-serif; font-weight: 700; font-size: 31px; line-height: 1;
  }
  .contact-list { position: absolute; list-style: none; font-size: 13px; }
  .contact-list li { display: flex; align-items: center; gap: 10px; height: 23px; }
  .contact-list--mail { left: 290px; top: 26px; }
  .contact-list--social { left: 529px; top: 25px; }
  .dot { width: 14px; height: 14px; border-radius: 50%; background: var(--icon); flex: none; }
</style>
</head>
<body>
<main class="flyer">
  <div class="photo photo--wrap" role="img" aria-label="Rollos de película estirable transparente"></div>
  <div class="photo photo--wood" role="img" aria-label="Vista interior de una tarima de madera"></div>
  <div class="photo photo--foam" role="img" aria-label="Rollo de espuma blanca sobre piso de madera"></div>
  <div class="photo photo--pallet" role="img" aria-label="Tarimas de madera apiladas"></div>

  <header class="brand">
    <div class="brand__name">LUMVEXA</div>
    <div class="brand__tag">Empaque Industrial</div>
  </header>

  <section class="section" style="top:174px">
    <h2 class="section__title">EMPRESA</h2>
    <div class="section__bar"></div>
    <p class="section__text">En LUMVEXA somos una empresa dedicada principalmente a la comercialización de productos de empaque industrial, con la idea de brindar precios muy competitivos en el mercado, logrando siempre mantener la calidad de nuestros productos, así como sus procesos formando un grupo de trabajo enfocado a la calidad, al servicio al cliente y sobre todo a la excelencia.</p>
  </section>

  <section class="section" style="top:426px">
    <h2 class="section__title">VISIÓN</h2>
    <div class="section__bar"></div>
    <p class="section__text">Ser lideres a nivel nacional en la comercialización de productos para empaque industrial, ser reconocidos por la calidad de los productos que ofrecemos y el excelente servicio de nuestro personal, logrando incrementar nuestro servicio a un mayor número de clientes a través de una búsqueda continua de productos que satisfagan la demanda de la industria.</p>
  </section>

  <section class="section" style="top:677px">
    <h2 class="section__title">MISIÓN</h2>
    <div class="section__bar"></div>
    <p class="section__text">Responder a la confianza que nuestros clientes depositan en nosotros, buscando su entera satisfacción, así como también una relación duradera basada en el compromiso y respeto.</p>
  </section>

  <section class="section" style="top:826px">
    <h2 class="section__title">VALORES</h2>
    <div class="section__bar"></div>
    <ul class="values">
      <li>Calidad</li><li>Honestidad</li>
      <li>Compromiso</li><li>Comunicación</li>
    </ul>
  </section>

  <footer class="contact-band">
    <div class="contact-phone">
      <svg width="22" height="40" viewBox="0 0 26 44" aria-hidden="true">
        <path d="M8 2 L14 2 L16 11 L11 14 Q9 22 11 30 L16 33 L14 42 L8 42 Q1 32 1 22 Q1 12 8 2 Z" fill="#4a4a4a"/>
      </svg>
      <span>(81) 4715-2083</span>
    </div>
    <ul class="contact-list contact-list--mail">
      <li>
        <svg width="16" height="11" viewBox="0 0 18 12" aria-hidden="true"><rect x="0.5" y="0.5" width="17" height="11" fill="none" stroke="#4a4a4a"/><path d="M0.5 0.5 L9 7 L17.5 0.5" fill="none" stroke="#4a4a4a"/></svg>
        ventas@lumvexa.com
      </li>
      <li>
        <svg width="16" height="16" viewBox="0 0 18 18" aria-hidden="true"><circle cx="9" cy="9" r="8" fill="#4a4a4a"/><circle cx="9" cy="8" r="3" fill="none" stroke="#fff" stroke-width="1.6"/></svg>
        Valle Arenal, Sierra Alta, México.
      </li>
    </ul>
    <ul class="contact-list contact-list--social">
      <li><span class="dot"></span>@LUMVEXAMTY</li>
      <li><span class="dot"></span>@lumvexamty</li>
    </ul>
  </footer>
</main>
</body>
</html>
```